Business card for Les Brisants-Corail campsite

HORIZONTAL / 85x55
OBJECTIVE
Create a modern, attractive and memorable business card for the Les Brisants-Corail campsite, located on the Île d'Oléron.
The map should make people want to discover the campsite and immediately convey its world: ocean, holidays, nature and conviviality.
VISUAL IDENTITY
The design must be in the same graphic style as our website:
www.lesbrisants-corail.fr
The site is the main reference for the visual atmosphere: colours, typography, shapes, photographs and general universe.
The map and the site must give the impression of belonging to a single brand identity.
A UNIVERSE TO TRANSMIT
• Île d'Oléron
• Atlantic Ocean
• Seaside
• Direct access to the beaches
• Vacation
• Nature
• Family-friendly and welcoming atmosphere
• Relaxation
DESIRED STYLE
Bright, warm, modern, nautical and natural.
We want a creation with a real personality, immediately recognizable, and not a generic camping business card.
FRONT
Prioritize visual impact with:
• Official logo Les Brisants-Corail
• Île d'Oléron
• A strong evocation of the ocean and holidays
• A short and memorable hook
The designer is free to propose their own hook.
BACK
The Coral Breakers
Villages 1 & 2
22 Rue des Mouettes
17880 Anse-aux-Goélands
France
Tel.: +33 5 47 12 38 04
www.lesbrisants-corail. fr
Possibility of discreet integration:
Direct access to the beaches
Mobile homes • Pitches • Accommodation
Le Varech Bar-Restaurant
FORMAT
Double-sided card: 85 × 55 mm.
Horizontal orientation
AVOID
• Overly institutional design
• Overloaded map
• Generic "camping" style
• Too many pictograms
• Accumulation of texts
• Modification or distortion of the official logo
• Graphic design unrelated to the website
CREATIVE FREEDOM
We are looking for an original proposal.
The designer can play with the graphic codes of the ocean, waves, sun, beach and Île d'Oléron, while remaining faithful to the visual identity of the site.
The card must be aesthetically pleasing and original enough to make people want to keep it.
The objective:
See the map → think about the ocean and holidays → remember Les Brisants-Corail → discover the campsite.
Target Market(s)
All targets
Industry/Entity Type
Tourisme
Contact Information for Business Card
adresse, téléphone, email, site internet + réseaux sociaux
Look and feel
Each slider illustrates characteristics of the customer's brand and the style your logo design should communicate.

```html
<!DOCTYPE html>
<html lang="fr">
<head>
<meta charset="utf-8">
<title>Les Brisants-Corail – carte de visite</title>
<link href="https://fonts.googleapis.com/css2?family=Poppins:wght@500;600&family=DM+Serif+Display&family=Kaushan+Script&family=Libre+Baskerville:wght@700&display=swap" rel="stylesheet">
<style>
  :root{
    --stage:#b3b3b3;
    --navy:#1b2940;
    --lime:#a9c51f;
    --lime-soft:#b8cf2d;
    --sky:#cfe3f2;
    --sea:#7f9fb5;
    --land:#6f8a4e;
    --white:#ffffff;
    --blue-pill:#2aa7df;
    --green-pill:#7cc242;
    --yellow:#e8e03a;
  }
  *{margin:0;padding:0;box-sizing:border-box}
  html,body{width:959px;height:1200px;overflow:hidden;background:var(--stage)}
  body{position:relative;font-family:"Poppins",sans-serif;color:var(--white)}
  .card{position:absolute;left:162px;width:634px;height:411px;overflow:hidden;background:var(--navy)}
  .card--front{top:132px}
  .card--back{top:653px}
  .card svg.shapes{position:absolute;inset:0}
  .abs{position:absolute;white-space:nowrap}

  /* front */
  .brand-name{font-weight:600;font-size:22px;letter-spacing:.5px;line-height:1.1}
  .brand-name small{display:block;font-size:10px;letter-spacing:3px;font-weight:500}
  .front-brand{left:36px;top:42px;color:var(--navy)}
  .hero-title{left:34px;top:262px;font-family:"DM Serif Display",serif;font-size:64px;line-height:1}
  .hero-script{left:196px;top:232px;font-family:"Kaushan Script",cursive;font-size:25px;line-height:1;color:var(--lime);transform:rotate(-6deg)}
  .tagline{left:34px;top:341px;font-size:14px;line-height:17px;font-weight:500;color:var(--lime);white-space:normal;width:270px}
  .rule{left:160px;top:370px;width:212px;height:1px;background:var(--white)}
  .front-url{left:380px;top:358px;font-size:16.5px;font-weight:500}
  .front-url span{color:var(--lime)}

  /* back */
  .back-brand{top:48px;color:var(--white);text-align:right}
  .back-brand--v1{left:74px}
  .back-brand--v2{left:366px}
  .village-pill{display:inline-block;margin-top:6px;padding:1px 12px;border-radius:8px;font-size:8px;letter-spacing:2px;font-weight:600;color:var(--white)}
  .village-pill--1{background:var(--blue-pill)}
  .village-pill--2{background:var(--green-pill)}
  .contact{left:66px;top:148px}
  .contact-row{display:flex;align-items:flex-start;gap:7px;font-size:14px;font-weight:500;line-height:16px;margin-bottom:7px}
  .contact-row svg{flex:none;width:16px;height:16px}
  .features{left:381px;top:146px}
  .features h3{font-family:"Libre Baskerville",serif;font-weight:700;font-size:15px;line-height:17px;color:var(--lime);width:200px;white-space:normal;margin-bottom:4px}
  .feature{display:flex;align-items:center;gap:6px;font-size:13.5px;font-weight:500;line-height:21px}
  .feature svg{width:11px;height:11px}
  .restaurant{margin-top:6px;font-size:17px;font-weight:600;letter-spacing:.5px}
  .follow{left:68px;top:350px;font-family:"Libre Baskerville",serif;font-weight:700;font-size:15px;color:var(--navy)}
  .back-url{left:275px;top:348px;font-size:16.5px;font-weight:500}
</style>
</head>
<body>

<section class="card card--front">
  <svg class="shapes" viewBox="0 0 634 411" width="634" height="411">
    <defs>
      <linearGradient id="landscape" x1="0" y1="0" x2="0" y2="1">
        <stop offset="0" stop-color="#eef5fb"/>
        <stop offset=".35" stop-color="var(--sky)"/>
        <stop offset=".5" stop-color="var(--sea)"/>
        <stop offset=".75" stop-color="var(--land)"/>
        <stop offset="1" stop-color="#8a7d6a"/>
      </linearGradient>
      <linearGradient id="beach" x1="0" y1="0" x2="0" y2="1">
        <stop offset="0" stop-color="#9cc3e4"/>
        <stop offset=".4" stop-color="#5f7d55"/>
        <stop offset=".7" stop-color="#d8c9a6"/>
        <stop offset="1" stop-color="#4f9a94"/>
      </linearGradient>
    </defs>
    <rect width="634" height="290" fill="url(#landscape)" role="img" aria-label="Photo aérienne du littoral avec village, prés et estran"/>
    <path d="M0 232 C120 210 260 205 400 236 C480 254 560 262 634 264 L634 411 L0 411Z" fill="var(--white)"/>
    <path d="M0 248 C130 228 260 222 400 246 C480 262 560 274 634 272 L634 411 L0 411Z" fill="var(--navy)"/>
    <circle cx="486" cy="259" r="79" fill="var(--lime-soft)"/>
    <circle cx="486" cy="259" r="74" fill="url(#beach)" role="img" aria-label="Photo aérienne d'une plage de sable et de l'océan"/>
  </svg>
  <div class="abs brand-name front-brand"><small>CAMPING ★★</small>Les Brisants-Corail</div>
  <div class="abs hero-title">Respirez</div>
  <div class="abs hero-script">l'air marin</div>
  <p class="abs tagline">Vivez l'expérience au Camping Les Brisants-Corail</p>
  <div class="abs rule"></div>
  <div class="abs front-url">www.<span>lesbrisants-corail</span>. fr</div>
</section>

<section class="card card--back">
  <svg class="shapes" viewBox="0 0 634 411" width="634" height="411">
    <path d="M0 303 C140 282 260 280 380 300 C470 316 530 350 634 358 L634 411 L0 411Z" fill="var(--white)"/>
    <path d="M0 331 C140 306 260 302 380 318 C470 330 530 362 634 366 L634 411 L0 411Z" fill="var(--lime)"/>
  </svg>

  <div class="abs brand-name back-brand back-brand--v1"><small>CAMPING ★★</small>Les Brisants-Corail<br><span class="village-pill village-pill--1">VILLAGE 1</span></div>
  <div class="abs brand-name back-brand back-brand--v2"><small>CAMPING ★★</small>Les Brisants-Corail<br><span class="village-pill village-pill--2">VILLAGE 2</span></div>

  <div class="abs contact">
    <div class="contact-row">
      <svg viewBox="0 0 16 16"><circle cx="8" cy="8" r="8" fill="var(--yellow)"/><path d="M5 4.5l1.6-.4 1 2-1 .8c.5 1 1.3 1.8 2.3 2.3l.8-1 2 1-.4 1.6c-3.2.2-6.5-3.1-6.3-6.3z" fill="var(--navy)"/></svg>
      <span>+33 547123804</span>
    </div>
    <div class="contact-row">
      <svg viewBox="0 0 16 16"><circle cx="8" cy="8" r="8" fill="var(--yellow)"/><path d="M8 3.5a3 3 0 0 1 3 3c0 2.2-3 5.5-3 5.5S5 8.7 5 6.5a3 3 0 0 1 3-3z" fill="var(--navy)"/><circle cx="8" cy="6.5" r="1.1" fill="var(--yellow)"/></svg>
      <span>22 Rue des Mouettes<br>17880 Anse-aux-Goélands<br>France</span>
    </div>
    <div class="contact-row">
      <svg viewBox="0 0 16 16"><circle cx="8" cy="8" r="8" fill="var(--yellow)"/><circle cx="8" cy="8" r="4" fill="none" stroke="var(--navy)" stroke-width="1.1"/><path d="M4 8h8M8 4c-1.6 2.4-1.6 5.6 0 8M8 4c1.6 2.4 1.6 5.6 0 8" fill="none" stroke="var(--navy)" stroke-width="1"/></svg>
      <span>www.lesbrisants-corail. fr</span>
    </div>
  </div>

  <div class="abs features">
    <h3>DIRECT ACCESS TO THE BEACHES</h3>
    <div class="feature"><svg viewBox="0 0 12 12"><circle cx="6" cy="6" r="6" fill="var(--yellow)"/><path d="M3.3 6.2l1.8 1.7 3.6-3.6" fill="none" stroke="var(--navy)" stroke-width="1.5"/></svg>Mobile homes</div>
    <div class="feature"><svg viewBox="0 0 12 12"><circle cx="6" cy="6" r="6" fill="var(--yellow)"/><path d="M3.3 6.2l1.8 1.7 3.6-3.6" fill="none" stroke="var(--navy)" stroke-width="1.5"/></svg>Pitches</div>
    <div class="feature"><svg viewBox="0 0 12 12"><circle cx="6" cy="6" r="6" fill="var(--yellow)"/><path d="M3.3 6.2l1.8 1.7 3.6-3.6" fill="none" stroke="var(--navy)" stroke-width="1.5"/></svg>Accommodation</div>
    <div class="restaurant">Le Varech</div>
  </div>

  <div class="abs follow">SUIVEZ -NOUS</div>
  <div class="abs back-url">www.lesbrisants-corail.fr</div>
</section>

</body>
</html>
```